Voltline Assemblies, Inc. Business Card

Voltline has three operating entities and I'm looking for a standard business card template that can be used for Voltline and the three operating entities that the logo just get swapped out, but has a very similar look and feel. Ultimately if someone had a business card from each, they assume the organizations are related because they all have the same look and feel.
Below are our websites and I will attached the logos for each entity:
https://www.voltlineassemblies.example/
https://www.brantoceramic.example/
https://www.omra-kfsd.example/
https://www.summitbreaker.example/

Target Market(s)

US Voltline

Industry/Entity Type

US Voltline

Contact Information for Business Card

Normal stuff

```html
<!DOCTYPE html>
<html lang="en">
<head>
<meta charset="utf-8">
<title>Voltline Assemblies, Inc. Business Card Family</title>
<link rel="stylesheet" href="https://fonts.googleapis.com/css2?family=Poppins:wght@400;500;600;700&display=swap">
<style>
  :root{
    --page:#e9eaee;
    --white:#ffffff;
    --ink:#1d1f2a;
    --volt-brand:#24306b;
    --volt-accent:#c8202f;
    --omra-brand:#272a78;
    --omra-accent:#272a78;
    --branto-brand:#2555a0;
    --branto-deep:#1c3d78;
    --branto-accent:#4a86d0;
    --summit-brand:#4e7a91;
    --summit-accent:#4e7a91;
  }
  *{margin:0;padding:0;box-sizing:border-box}
  html,body{width:1200px;height:900px;overflow:hidden}
  body{background:var(--page);font-family:"Poppins",sans-serif;color:var(--ink)}
  .card-family{display:grid;grid-template-columns:600px 600px;grid-template-rows:450px 450px;width:1200px;height:900px}
  .card-set{position:relative}

  .volt{--brand:var(--volt-brand);--accent:var(--volt-accent);--title:var(--volt-accent);--back:var(--volt-brand)}
  .omra{--brand:var(--omra-brand);--accent:var(--omra-accent);--title:#ffffff;--back:var(--omra-brand)}
  .branto{--brand:var(--branto-brand);--accent:var(--branto-accent);--title:var(--branto-accent);--back:linear-gradient(135deg,var(--branto-deep),var(--branto-brand))}
  .summit{--brand:var(--summit-brand);--accent:var(--summit-accent);--title:#ffffff;--back:var(--summit-brand)}

  .card{position:absolute;width:350px;height:200px;border-radius:12px;overflow:hidden;box-shadow:0 6px 16px rgba(20,24,40,.22)}
  .card-back{left:185px;top:18px;background:var(--back);color:var(--white);display:flex;flex-direction:column;align-items:center;justify-content:center;text-align:center}
  .card-front{left:65px;top:236px;background:var(--white)}

  .back-mark{display:flex;align-items:center;gap:8px}
  .mark-dot{width:22px;height:22px;border-radius:50%;background:var(--white);flex:none}
  .back-name{font-size:19px;font-weight:700;letter-spacing:.5px;text-transform:uppercase}
  .back-tagline{font-size:7px;margin-top:4px;letter-spacing:.3px}
  .back-web{font-size:8px;margin-top:16px;letter-spacing:1.4px;text-transform:uppercase}

  .front-shapes{position:absolute;inset:0;width:350px;height:200px}
  .shape-brand{fill:var(--brand)}
  .shape-accent{fill:var(--accent)}
  .shape-line{stroke:var(--accent);stroke-width:2}

  .holder{position:absolute;left:16px;top:11px;color:var(--white)}
  .holder-name{font-size:13px;font-weight:600;letter-spacing:.4px;text-transform:uppercase}
  .holder-title{font-size:8.5px;color:var(--title);text-transform:uppercase;letter-spacing:.3px;margin-top:-1px}

  .contact-list{position:absolute;left:16px;top:72px;list-style:none;font-size:8px;line-height:12.5px}
  .contact-list li{display:flex;align-items:center;gap:5px}
  .contact-icon{width:7px;height:7px;flex:none}
  .contact-icon *{fill:none;stroke:var(--accent);stroke-width:1.4}

  .front-mark{position:absolute;right:18px;top:106px;text-align:right;color:var(--brand)}
  .front-mark-row{display:flex;align-items:center;justify-content:flex-end;gap:6px}
  .front-mark .mark-dot{background:var(--accent);width:16px;height:16px}
  .front-name{font-size:12px;line-height:18px;font-weight:700;text-transform:uppercase;letter-spacing:.4px;white-space:nowrap}
  .front-tagline{font-size:6.5px;line-height:9px;margin-top:1px;white-space:nowrap}

  .address{position:absolute;right:18px;top:140px;text-align:right;font-size:8.5px;line-height:12px;font-weight:500;font-style:normal}
</style>
</head>
<body>
<main class="card-family">

  <section class="card-set volt">
    <div class="card card-back">
      <div class="back-mark"><span class="mark-dot"></span><span class="back-name">Voltline</span></div>
      <p class="back-tagline">Assemblies, Inc.</p>
      <p class="back-web">www.voltlineassemblies.example</p>
    </div>
    <div class="card card-front">
      <svg class="front-shapes" viewBox="0 0 350 200" aria-hidden="true">
        <polygon class="shape-brand" points="0,0 350,0 350,96 0,44"/>
        <line class="shape-line" x1="0" y1="51" x2="350" y2="103"/>
        <polygon class="shape-accent" points="0,190 110,190 110,200 0,200"/>
        <polygon class="shape-brand" points="110,190 122,182 350,182 350,200 110,200"/>
      </svg>
      <div class="holder"><p class="holder-name">Dale Hartwell</p><p class="holder-title">CEO / Board Member</p></div>
      <ul class="contact-list">
        <li><svg class="contact-icon" viewBox="0 0 8 8"><circle cx="4" cy="4" r="3"/></svg>555-201-4410</li>
        <li><svg class="contact-icon" viewBox="0 0 8 8"><rect x="1" y="1" width="6" height="6"/></svg>555-201-4412</li>
        <li><svg class="contact-icon" viewBox="0 0 8 8"><rect x="1" y="2" width="6" height="4"/><path d="M1 2 L4 4.5 L7 2"/></svg>info@voltlineassemblies.example</li>
        <li><svg class="contact-icon" viewBox="0 0 8 8"><circle cx="4" cy="4" r="3"/><path d="M1 4 H7"/></svg>www.voltlineassemblies.example</li>
      </ul>
      <div class="front-mark">
        <div class="front-mark-row"><span class="mark-dot"></span><span class="front-name">Voltline</span></div>
        <p class="front-tagline">Assemblies, Inc.</p>
      </div>
      <address class="address">2180 Ridgeview Drive<br>Suite 240<br>Fairhaven, AL 35099</address>
    </div>
  </section>

  <section class="card-set omra">
    <div class="card card-back">
      <div class="back-mark"><span class="mark-dot"></span><span class="back-name">Omra</span></div>
      <p class="back-tagline">Field Systems Division · A Voltline Assemblies, Inc. Company</p>
      <p class="back-web">www.omra-kfsd.example</p>
    </div>
    <div class="card card-front">
      <svg class="front-shapes" viewBox="0 0 350 200" aria-hidden="true">
        <polygon class="shape-brand" points="0,0 350,0 350,96 0,44"/>
        <line class="shape-line" x1="0" y1="51" x2="350" y2="103"/>
        <polygon class="shape-accent" points="0,190 110,190 110,200 0,200"/>
        <polygon class="shape-brand" points="110,190 122,182 350,182 350,200 110,200"/>
      </svg>
      <div class="holder"><p class="holder-name">Dale Hartwell</p><p class="holder-title">CEO / Board Member</p></div>
      <ul class="contact-list">
        <li><svg class="contact-icon" viewBox="0 0 8 8"><circle cx="4" cy="4" r="3"/></svg>555-201-4410</li>
        <li><svg class="contact-icon" viewBox="0 0 8 8"><rect x="1" y="1" width="6" height="6"/></svg>555-201-4412</li>
        <li><svg class="contact-icon" viewBox="0 0 8 8"><rect x="1" y="2" width="6" height="4"/><path d="M1 2 L4 4.5 L7 2"/></svg>info@omra-kfsd.example</li>
        <li><svg class="contact-icon" viewBox="0 0 8 8"><circle cx="4" cy="4" r="3"/><path d="M1 4 H7"/></svg>www.omra-kfsd.example</li>
      </ul>
      <div class="front-mark">
        <div class="front-mark-row"><span class="mark-dot"></span><span class="front-name">Omra</span></div>
        <p class="front-tagline">Field Systems Division · A Voltline Assemblies, Inc. Company</p>
      </div>
      <address class="address">2180 Ridgeview Drive<br>Suite 240<br>Fairhaven, AL 35099</address>
    </div>
  </section>

  <section class="card-set branto">
    <div class="card card-back">
      <div class="back-mark"><span class="mark-dot"></span><span class="back-name">Branto Ceramic, LLC</span></div>
      <p class="back-tagline">A Voltline Assemblies, Inc. Company</p>
      <p class="back-web">www.brantoceramic.example</p>
    </div>
    <div class="card card-front">
      <svg class="front-shapes" viewBox="0 0 350 200" aria-hidden="true">
        <defs>
          <linearGradient id="branto-fade" x1="0" y1="0" x2="1" y2="0">
            <stop offset="0" stop-color="#ffffff"/>
            <stop offset="1" stop-color="#4a86d0"/>
          </linearGradient>
        </defs>
        <polygon class="shape-brand" points="0,0 350,0 350,96 0,44"/>
        <line class="shape-line" x1="0" y1="51" x2="350" y2="103"/>
        <polygon fill="url(#branto-fade)" points="0,190 110,190 110,200 0,200"/>
        <polygon class="shape-brand" points="110,190 122,182 350,182 350,200 110,200"/>
      </svg>
      <div class="holder"><p class="holder-name">Dale Hartwell</p><p class="holder-title">CEO / Board Member</p></div>
      <ul class="contact-list">
        <li><svg class="contact-icon" viewBox="0 0 8 8"><circle cx="4" cy="4" r="3"/></svg>555-201-4410</li>
        <li><svg class="contact-icon" viewBox="0 0 8 8"><rect x="1" y="1" width="6" height="6"/></svg>555-201-4412</li>
        <li><svg class="contact-icon" viewBox="0 0 8 8"><rect x="1" y="2" width="6" height="4"/><path d="M1 2 L4 4.5 L7 2"/></svg>info@omra-kfsd.example</li>
        <li><svg class="contact-icon" viewBox="0 0 8 8"><circle cx="4" cy="4" r="3"/><path d="M1 4 H7"/></svg>www.omra-kfsd.example</li>
      </ul>
      <div class="front-mark">
        <div class="front-mark-row"><span class="mark-dot"></span><span class="front-name">Branto Ceramic, LLC</span></div>
        <p class="front-tagline">A Voltline Assemblies, Inc. Company</p>
      </div>
      <address class="address">2180 Ridgeview Drive<br>Suite 240<br>Fairhaven, AL 35099</address>
    </div>
  </section>

  <section class="card-set summit">
    <div class="card card-back">
      <div class="back-mark"><span class="mark-dot"></span><span class="back-name">Summit Breaker</span></div>
      <p class="back-tagline">A Voltline Assemblies Inc. Company</p>
      <p class="back-web">www.brantoceramic.example</p>
    </div>
    <div class="card card-front">
      <svg class="front-shapes" viewBox="0 0 350 200" aria-hidden="true">
        <polygon class="shape-brand" points="0,0 350,0 350,96 0,44"/>
        <line class="shape-line" x1="0" y1="51" x2="350" y2="103"/>
        <polygon class="shape-accent" points="0,190 110,190 110,200 0,200"/>
        <polygon class="shape-brand" points="110,190 122,182 350,182 350,200 110,200"/>
      </svg>
      <div class="holder"><p class="holder-name">Dale Hartwell</p><p class="holder-title">CEO / Board Member</p></div>
      <ul class="contact-list">
        <li><svg class="contact-icon" viewBox="0 0 8 8"><circle cx="4" cy="4" r="3"/></svg>555-201-4410</li>
        <li><svg class="contact-icon" viewBox="0 0 8 8"><rect x="1" y="1" width="6" height="6"/></svg>555-201-4412</li>
        <li><svg class="contact-icon" viewBox="0 0 8 8"><rect x="1" y="2" width="6" height="4"/><path d="M1 2 L4 4.5 L7 2"/></svg>info@omra-kfsd.example</li>
        <li><svg class="contact-icon" viewBox="0 0 8 8"><circle cx="4" cy="4" r="3"/><path d="M1 4 H7"/></svg>www.omra-kfsd.example</li>
      </ul>
      <div class="front-mark">
        <div class="front-mark-row"><span class="mark-dot"></span><span class="front-name">Summit Breaker</span></div>
        <p class="front-tagline">A Voltline Assemblies Inc. Company</p>
      </div>
      <address class="address">2180 Ridgeview Drive<br>Suite 240<br>Fairhaven, AL 35099</address>
    </div>
  </section>

</main>
</body>
</html>
```